TV+Music+Social Network+Entertainment+brightlistin= Designers lol

TV+ Music+ Social Network +Entertainment+ brightlistin=

ZELLOPAK.COM

Zellopak is a one-stop shop promotional plateform that will communicate information to all user of what is COOL, NEW and Exicting in your Neighborhood.(News,Events,Entertainment,ect) We promote for all User/Entrepreneur/business/Talents.We are the future and dream destination for all to whom owns a computer. Forming the the World Wide Web into your Local Wide Web. (Atlanta, Dallas, Las Vegas, New York ect.)

* EX: ( WWW. ??? .com =LWW. ??? .com)
WORLD = LOCAL

* Goal/Mission: Have customer/user visit the website and then leave their house to go experience life in their respective surroundings.

/////////////////////////Web page///////////////////////

Colors:Blue/Green/black

include: interchangable background picture @ top (to update easily and keep fresh) On this background picture include logo (top left) login/sign (top left)

Major Tabs: Music/Daylife/Nightlife/Video/Shop

Industry/Entity Type

House

Requirements
Nice to have
• Tv screen/search engine

```html
<!DOCTYPE html>
<html lang="en">
<head>
<meta charset="utf-8">
<title>Zellopak – What's going on in your neighborhood</title>
<link rel="stylesheet" href="https://fonts.googleapis.com/css2?family=Open+Sans:wght@400;600;700&display=swap">
<style>
:root{
  --ink:#111;
  --night:#0b0b10;
  --blue:#1e90e0;
  --blue-light:#3ba9f0;
  --green:#5cb82a;
  --green-dark:#3f8f15;
  --lime:#7cc42a;
  --white:#fff;
  --grey-text:#555;
  --tag-border:#dcdcdc;
  --footer-text:#d8d8d8;
}
*{box-sizing:border-box;margin:0;padding:0}
html,body{width:1045px;height:1200px;overflow:hidden}
body{font-family:"Open Sans",Arial,sans-serif;color:var(--ink);position:relative;background:var(--night)}
.backdrop{position:absolute;inset:0;background:
  radial-gradient(ellipse at 20% 20%,rgba(170,40,70,.55),transparent 45%),
  radial-gradient(ellipse at 85% 25%,rgba(200,60,110,.45),transparent 40%),
  radial-gradient(ellipse at 50% 30%,rgba(90,80,110,.6),transparent 60%),
  linear-gradient(180deg,#2a2430 0%,#3a2a28 35%,#2a1a12 70%,#140c08 100%)}
.site-header{position:absolute;left:115px;top:0;width:815px;height:87px;background:linear-gradient(#1a1a1a,#060606);border-bottom:2px solid var(--blue)}
.brand{position:absolute;left:30px;top:22px;display:flex;align-items:center;gap:10px;color:var(--white);font-size:34px;font-weight:600;letter-spacing:.5px}
.brand-dot{width:40px;height:40px;border-radius:50%;background:var(--blue)}
.main-nav{position:absolute;right:20px;top:32px;display:flex;gap:22px}
.main-nav a{color:var(--white);text-decoration:none;font-size:17px;font-weight:600}
.main-nav a.active{color:var(--blue-light)}
.nav-pointer{position:absolute;left:547px;top:80px}
.account-tab{position:absolute;left:935px;top:0;width:64px;height:87px;background:var(--green);padding:8px 0 0 12px}
.account-tab a{display:block;color:var(--white);font-size:8px;font-weight:600;text-decoration:none;line-height:19px;border-bottom:1px solid rgba(255,255,255,.25);width:44px}
.hero{position:absolute;left:115px;top:89px;width:815px;height:314px;background:linear-gradient(180deg,rgba(0,0,0,.15),rgba(0,0,0,.35))}
.hero-title{position:absolute;left:84px;top:44px;color:var(--white);font-weight:600;line-height:1.05;text-transform:uppercase}
.hero-title .l1{font-size:44px;text-transform:none}
.hero-title .l1 em{font-style:normal;font-size:27px;color:var(--lime);text-transform:uppercase}
.hero-title .l2{font-size:42px}
.hero-copy{position:absolute;left:84px;top:160px;color:#eee;font-size:14px;line-height:27px}
.cta{position:absolute;left:84px;top:225px;width:216px;height:44px;background:linear-gradient(#6fc63a,var(--green-dark));border:1px solid #8bd45a;color:var(--white);font-size:21px;display:flex;align-items:center;justify-content:center;gap:10px}
.hero-thumbs{position:absolute;left:609px;top:65px;display:flex;gap:6px}
.hero-thumbs span{width:50px;height:52px;border:2px solid var(--white)}
.slide-arrow{position:absolute;top:205px}
.panel{position:absolute;left:115px;top:403px;width:815px;height:582px;background:var(--white)}
.promo{position:absolute;top:18px;width:245px;height:82px;display:flex;align-items:center;gap:14px;padding-left:24px;color:var(--white);box-shadow:0 3px 4px rgba(0,0,0,.35)}
.promo b{font-weight:400;font-size:14px;display:block}
.promo small{font-size:11.5px;text-decoration:underline}
.promo-events{left:21px;background:linear-gradient(90deg,#111 20%,#a0861a)}
.promo-videos{left:285px;background:linear-gradient(90deg,#111 20%,#1f6f78)}
.promo-fun{left:549px;background:linear-gradient(90deg,#111 20%,#4d8a17)}
.section-title{position:absolute;font-size:16px;font-weight:400}
.rule{position:absolute;height:3px;background:var(--ink)}
.rule::before{content:"";position:absolute;left:0;top:0;width:95px;height:3px;background:var(--blue)}
.tile{position:absolute;width:228px;height:107px}
.tile-caption{position:absolute;left:0;bottom:0;width:100%;height:28px;background:rgba(0,0,0,.6);color:var(--white);font-weight:700;font-size:15px;display:flex;align-items:center;gap:6px;padding-left:14px}
.tweet{position:absolute;left:21px;top:490px;width:484px;font-size:10.5px;line-height:15px;color:var(--grey-text)}
.tweet strong{display:block;color:var(--ink);font-size:11px;margin-bottom:3px}
.tweet a{color:var(--blue);text-decoration:none}
.divider{position:absolute;left:528px;top:127px;height:425px;border-left:1px dashed #ccc}
.feature-photo{position:absolute;left:548px;top:127px;width:245px;height:205px;background:radial-gradient(ellipse at 50% 30%,#ffcf5a,#d55a10 55%,#2a0c04)}
.aside-title{position:absolute;left:548px;top:353px;font-size:14.5px;line-height:18px;font-weight:400}
.tags{position:absolute;left:548px;top:413px;width:250px;display:flex;flex-wrap:wrap;gap:8px 6px}
.tags span{font-size:10px;color:#666;border:1px solid var(--tag-border);border-radius:3px;padding:3px 5px;line-height:12px}
.site-footer{position:absolute;left:115px;top:1015px;width:815px}
.footer-nav{display:flex;gap:12px;font-size:10.5px}
.footer-nav a{color:var(--footer-text);text-decoration:none}
.footer-nav a.active{color:var(--blue-light)}
.footer-rule{position:absolute;left:0;top:26px;width:540px;border-top:1px solid #555}
.footer-legal{position:absolute;left:0;top:40px;font-size:10.5px;color:var(--footer-text);white-space:nowrap}
.social{position:absolute;left:478px;top:0;display:flex;gap:5px}
.social span{width:15px;height:15px;background:var(--white);border-radius:2px}
.footer-brand{position:absolute;right:0;top:6px;font-size:28px;font-weight:600;color:rgba(255,255,255,.22)}
</style>
</head>
<body>
<div class="backdrop" role="img" aria-label="Interchangeable background photo of a busy neon-lit city street at night with a crowd below"></div>

<header class="site-header">
  <div class="brand"><span class="brand-dot"></span>zellopak</div>
  <nav class="main-nav">
    <a href="#">Music</a><a href="#" class="active">Daylife</a><a href="#">Nightlife</a><a href="#">Video</a><a href="#">Shop</a>
  </nav>
  <svg class="nav-pointer" width="14" height="8" viewBox="0 0 14 8"><path d="M0 8 7 0 14 8z" fill="var(--blue)"/></svg>
</header>

<div class="account-tab"><a href="#">SIGN IN</a><a href="#">SIGN UP</a><a href="#">HELP</a><a href="#">CONTACT</a></div>

<section class="hero">
  <h1 class="hero-title"><span class="l1">zellopak!! <em>Whats going on in</em></span><br><span class="l2">Your Nieghborhood?</span></h1>
  <p class="hero-copy">Zellopak is a one-stop shop promotional platform...<br>Will communicate information to all users...</p>
  <a class="cta">Get Start Now
    <svg width="20" height="20" viewBox="0 0 20 20"><circle cx="10" cy="10" r="8.5" fill="none" stroke="#fff" stroke-width="2"/><path d="M8 6l5 4-5 4z" fill="#fff"/></svg></a>
  <div class="hero-thumbs">
    <span role="img" aria-label="City photo" style="background:linear-gradient(135deg,#c2203a,#2040a0)"></span>
    <span role="img" aria-label="Event photo" style="background:linear-gradient(135deg,#3b6fd0,#d03a9a)"></span>
    <span role="img" aria-label="Portrait photo" style="background:linear-gradient(135deg,#ddd,#556)"></span>
  </div>
</section>
<svg class="slide-arrow" style="left:45px" width="30" height="50" viewBox="0 0 30 50"><path d="M26 3 5 25l21 22" fill="none" stroke="rgba(255,255,255,.6)" stroke-width="5"/></svg>
<svg class="slide-arrow" style="left:972px" width="30" height="50" viewBox="0 0 30 50"><path d="M4 3l21 22L4 47" fill="none" stroke="rgba(255,255,255,.6)" stroke-width="5"/></svg>

<main class="panel">
  <a class="promo promo-events">
    <svg width="34" height="34" viewBox="0 0 34 34"><circle cx="17" cy="17" r="15" fill="#e0b520"/><path d="M17 8v10h7" stroke="#222" stroke-width="3" fill="none"/></svg>
    <span><b>See Popular Events</b><small>Click Here to More Info...</small></span></a>
  <a class="promo promo-videos">
    <svg width="30" height="32" viewBox="0 0 30 32"><rect x="2" y="1" width="26" height="30" fill="#3cb6c6"/><g fill="#111"><rect x="5" y="4" width="3" height="4"/><rect x="5" y="12" width="3" height="4"/><rect x="5" y="20" width="3" height="4"/><rect x="22" y="4" width="3" height="4"/><rect x="22" y="12" width="3" height="4"/><rect x="22" y="20" width="3" height="4"/><rect x="11" y="4" width="8" height="24"/></g></svg>
    <span><b>Watch Popular Videos</b><small>Click Here to More Info...</small></span></a>
  <a class="promo promo-fun">
    <svg width="38" height="32" viewBox="0 0 38 32"><path d="M5 22a14 14 0 0 1 28 0" fill="none" stroke="#7fd43a" stroke-width="4"/><rect x="2" y="18" width="8" height="13" rx="2" fill="#7fd43a"/><rect x="28" y="18" width="8" height="13" rx="2" fill="#7fd43a"/></svg>
    <span><b>Find Entertainment</b><small>Click Here to More Info...</small></span></a>

  <div class="divider"></div>

  <h2 class="section-title" style="left:21px;top:121px">Featured Services</h2>
  <div class="rule" style="left:21px;top:154px;width:484px"></div>

  <div class="tile" style="left:21px;top:175px;background:linear-gradient(135deg,#2a3a8a,#c53c7a 50%,#e8b030)" role="img" aria-label="Photo of a neon-lit city square">
    <div class="tile-caption"><svg width="14" height="14" viewBox="0 0 14 14"><circle cx="7" cy="7" r="7" fill="#fff"/><path d="M7 3.5v7M3.5 7h7" stroke="#000" stroke-width="2"/></svg>Featured Services</div></div>
  <div class="tile" style="left:276px;top:175px;background:linear-gradient(90deg,#3a3a3a,#8a8a70 50%,#f1df1a)" role="img" aria-label="Photo of an electronics store front">
    <div class="tile-caption"><svg width="14" height="14" viewBox="0 0 14 14"><circle cx="7" cy="7" r="7" fill="#fff"/><path d="M7 3.5v7M3.5 7h7" stroke="#000" stroke-width="2"/></svg>Featured Services</div></div>
  <div class="tile" style="left:21px;top:305px;background:linear-gradient(90deg,#c9a06a,#8a6a48 60%,#3a3a3a)" role="img" aria-label="Photo of a smartphone unboxing">
    <div class="tile-caption"><svg width="14" height="14" viewBox="0 0 14 14"><circle cx="7" cy="7" r="7" fill="#fff"/><path d="M7 3.5v7M3.5 7h7" stroke="#000" stroke-width="2"/></svg>Featured Services</div></div>
  <div class="tile" style="left:276px;top:305px;background:linear-gradient(90deg,#d8d0c8,#3a2e28 40%,#0a0a0a)" role="img" aria-label="Promotional photo of a music artist">
    <div class="tile-caption"><svg width="14" height="14" viewBox="0 0 14 14"><circle cx="7" cy="7" r="7" fill="#fff"/><path d="M7 3.5v7M3.5 7h7" stroke="#000" stroke-width="2"/></svg>Featured Services</div></div>

  <h2 class="section-title" style="left:21px;top:440px;display:flex;align-items:center;gap:10px"><span style="width:20px;height:20px;background:var(--ink);border-radius:50%"></span>Zellopak on Chirper</h2>
  <div class="rule" style="left:21px;top:473px;width:484px"></div>
  <div class="tweet"><strong>Marcus Dellow</strong>Lorem Ipsum is simply dummy text of the printing and typesetting industry. Lorem Ipsum has been the industry's standard dummy.. <a href="#">http://zl.co/plug123/ &nbsp;| &nbsp;05/02/2012 5:44 PM</a></div>

  <div class="feature-photo" role="img" aria-label="Concert photo of a crowd before a lit stage, Stageroom Music promotion"></div>
  <h3 class="aside-title">We are the Future and Dream<br>Destination for</h3>
  <div class="rule" style="left:548px;top:400px;width:245px"></div>
  <div class="tags">
    <span>Greenland</span><span>nailed</span><span>watersland</span><span>Standared</span>
    <span>watersland</span><span>Standared</span><span>Greenland</span><span>nailed</span>
    <span>dummy Standared</span><span>Greenland</span><span>nailed</span><span>led</span>
    <span>Batmanto</span><span>watersland</span><span>Standared</span><span>nailed</span>
  </div>
</main>

<footer class="site-footer">
  <nav class="footer-nav"><a href="#">Home</a><a href="#">About</a><a href="#">Music</a><a href="#" class="active">Daylife</a><a href="#">Nightlife</a><a href="#">Video</a><a href="#">Shop</a><a href="#">Contact</a></nav>
  <div class="social"><span></span><span></span><span></span></div>
  <div class="footer-rule"></div>
  <p class="footer-legal">All Right Reserved © Copyright 2012 - zellopak.com &nbsp;| Privacy Policy | Terms of Use</p>
  <div class="footer-brand">zellopak</div>
</footer>
</body>
</html>
```